Business Name is TL Glamworks - Make-up Artist

I'm looking for an attractive and eye catching business card for for mobile make-up artist business. On the front of the card, I just want the name TL Glamworks in feminine type cursive writing and underneath my name Tessa Lowrie and Make-Up Artist.
On the back of the card, I would like written down one side the following;
Make-Up Tutorials
Bridal
Photography
Debutante
Formals
Family Portraits
I would also like the following details as well as the Chatterbook and Snapgram Icons;
Mobile: 0462 318 725
Email: tessalowrie@mailbox-demo.com
Website: tessalowrie.velmora-demo.com
Certificate III in Make-Up
Also, I would like a section that says Your Next Appointment and a space to put that information.
I would also like the Velmora Symbol on the bottom right hand corner (I have attached)

Target Market(s)

Mostly females

Industry/Entity Type

Makeup

Contact Information for Business Card

TL Glamworks
Tessa Lowrie - Make-Up Artist

Font styles to use
Script

Colors
b768aa
886aae
e34297

Requirements
Must have
• Mobile: 0462 318 725
• Email: tessalowrie@mailbox-demo.com
• Website: tessalowrie.velmora-demo.com
• Certificate III in Make-Up
Nice to have
• Something to do with make-up like a smudged lipstick or some eye shadow
Should not have
• Don't want it too busy

```html
<!DOCTYPE html>
<html lang="en">
<head>
<meta charset="utf-8">
<title>TL Glamworks – Business Card</title>
<link rel="stylesheet" href="https://fonts.googleapis.com/css2?family=Great+Vibes&family=Josefin+Sans:wght@300;400&family=Lato:wght@400;700&display=swap">
<style>
  :root {
    --backdrop: #560030;
    --card-pink: #e0449a;
    --brand-pink: #e8449b;
    --white: #ffffff;
    --soft-grey: #d8d8d8;
    --rule: rgba(255, 255, 255, 0.75);
  }
  html, body {
    margin: 0;
    padding: 0;
    overflow: hidden;
  }
  .canvas {
    position: relative;
    width: 1200px;
    height: 900px;
    background: var(--backdrop);
    overflow: hidden;
  }
  .card {
    position: absolute;
    top: 215px;
    width: 414px;
    height: 414px;
    border-radius: 50%;
    overflow: hidden;
    box-shadow: 0 3px 8px rgba(0, 0, 0, 0.35);
  }
  .card--front { left: 164px; }
  .card--back {
    left: 623px;
    background: var(--card-pink);
    color: var(--white);
    font-family: "Lato", sans-serif;
    text-align: center;
  }
  .card__photo {
    position: absolute;
    inset: 0;
    display: block;
  }
  .front__title {
    position: absolute;
    left: 0;
    right: 0;
    top: 222px;
    margin: 0;
    text-align: center;
    font-family: "Great Vibes", cursive;
    font-weight: 400;
    font-size: 54px;
    line-height: 1;
    color: var(--brand-pink);
    padding-left: 36px;
  }
  .front__role {
    position: absolute;
    left: 0;
    right: 0;
    top: 284px;
    margin: 0;
    text-align: center;
    font-family: "Josefin Sans", sans-serif;
    font-weight: 300;
    font-size: 17px;
    letter-spacing: 0.3px;
    color: var(--soft-grey);
    padding-left: 30px;
  }
  .front__cert {
    position: absolute;
    left: 0;
    right: 0;
    top: 320px;
    margin: 0;
    text-align: center;
    font-family: "Lato", sans-serif;
    font-size: 19px;
    color: var(--brand-pink);
    padding-left: 0;
  }
  .services {
    position: absolute;
    top: 58px;
    left: 0;
    right: 0;
    margin: 0;
    font-size: 19.5px;
    line-height: 24px;
    text-shadow: 0 1px 2px rgba(0, 0, 0, 0.25);
  }
  .divider {
    position: absolute;
    left: 89px;
    width: 236px;
    height: 22px;
  }
  .divider--contact { top: 159px; }
  .divider--brand { top: 293px; }
  .contact {
    position: absolute;
    top: 187px;
    left: 0;
    right: 0;
    margin: 0;
    font-size: 19.5px;
    line-height: 24.5px;
    text-shadow: 0 1px 2px rgba(0, 0, 0, 0.2);
  }
  .brand {
    position: absolute;
    top: 278px;
    left: 0;
    right: 0;
    display: flex;
    flex-direction: column;
    align-items: center;
    gap: 6px;
  }
  .brand__mark {
    width: 34px;
    height: 34px;
    border-radius: 50%;
    background: var(--white);
  }
  .brand__name {
    font-family: "Lato", sans-serif;
    font-weight: 700;
    font-size: 12px;
    letter-spacing: 1px;
    color: var(--white);
    text-transform: uppercase;
  }
</style>
</head>
<body>
<main class="canvas">

  <section class="card card--front" aria-label="Card front">
    <svg class="card__photo" width="414" height="414" viewBox="0 0 414 414" role="img" aria-label="Close-up photograph of a woman with dark hair applying pink lipstick">
      <defs>
        <radialGradient id="photo-tone" cx="0.25" cy="0.25" r="0.8">
          <stop offset="0" stop-color="#b88a7c"/>
          <stop offset="0.3" stop-color="#6a4a44"/>
          <stop offset="0.65" stop-color="#2a2322"/>
          <stop offset="1" stop-color="#161313"/>
        </radialGradient>
      </defs>
      <rect width="414" height="414" fill="url(#photo-tone)"/>
      <rect y="383" width="414" height="31" fill="#050505"/>
      <rect width="414" height="414" fill="rgba(0,0,0,0.25)"/>
    </svg>
    <h1 class="front__title">TL Glamworks</h1>
    <p class="front__role">TESSA LOWRIE - MAKE-UP ARTIST</p>
    <p class="front__cert">Certificate III in Make-Up</p>
  </section>

  <section class="card card--back" aria-label="Card back">
    <p class="services">Make-Up Tutorials | Bridal<br>Photography | Debutante<br>Formals | Family Portraits</p>

    <svg class="divider divider--contact" viewBox="0 0 236 22" aria-hidden="true">
      <line x1="0" y1="11" x2="80" y2="11" stroke="var(--rule)" stroke-width="1"/>
      <line x1="156" y1="11" x2="236" y2="11" stroke="var(--rule)" stroke-width="1"/>
      <g class="icon icon--phone">
        <circle cx="93" cy="11" r="10.5" fill="var(--white)"/>
        <rect x="89" y="4.5" width="8" height="13" rx="1.5" fill="none" stroke="var(--card-pink)" stroke-width="1.6"/>
        <circle cx="93" cy="15" r="0.9" fill="var(--card-pink)"/>
      </g>
      <g class="icon icon--mail">
        <circle cx="118" cy="11" r="10.5" fill="var(--white)"/>
        <rect x="111.5" y="6.5" width="13" height="9" fill="var(--card-pink)"/>
        <polyline points="111.5,6.5 118,12 124.5,6.5" fill="none" stroke="var(--white)" stroke-width="1.2"/>
      </g>
      <g class="icon icon--globe">
        <circle cx="143" cy="11" r="10.5" fill="var(--white)"/>
        <circle cx="143" cy="11" r="6.5" fill="var(--card-pink)"/>
        <ellipse cx="143" cy="11" rx="2.8" ry="6.5" fill="none" stroke="var(--white)" stroke-width="1"/>
        <line x1="136.5" y1="11" x2="149.5" y2="11" stroke="var(--white)" stroke-width="1"/>
      </g>
    </svg>

    <p class="contact">0462 318 725<br>tessalowrie@mailbox-demo.com<br>tessalowrie.velmora-demo.com</p>

    <svg class="divider divider--brand" viewBox="0 0 236 22" aria-hidden="true">
      <line x1="0" y1="11" x2="92" y2="11" stroke="var(--rule)" stroke-width="1"/>
      <line x1="144" y1="11" x2="236" y2="11" stroke="var(--rule)" stroke-width="1"/>
    </svg>

    <div class="brand">
      <span class="brand__mark" aria-hidden="true"></span>
      <span class="brand__name">Velmora</span>
    </div>
  </section>

</main>
</body>
</html>
```